A QUIET WREN SANG

Double sided heavy linen business card. On the front an abstract of one of my floral arrangements and on the back an abstract of myself with the white three button butlers jacket.The front should be printed with a quiet wren sang with a mid century modern font and the reverse should simply say bespoke home services with the same font, my name Dov Renko, 555 203 4417 and ferrow tendle.com PO box4082 Bridlemoor, kt 11907. The entire card should evoke a mid century modern style with Brendan Quisholm, Teddy Morvik's, R J Halbern and Nora Fenstadt style. I want it to be retro crazy. No -dashes anywhere.

Target Market(s)

The one percent

Industry/Entity Type

Business

Font styles to use
Other font styles liked:
• Mid century modern

Requirements
Must have
• Colorful mid century modern designs. A floral front and a white jacketed butler based on my picture on the reverse. The font should be based on a mid century design.
Nice to have
• Mid century modern with the designers I mentioned above with clear regiimented spacing with my phone number, website, etc.
Should not have
• Nothing pertaining with what I do. That is why I want Bespoke Home Services printed on the back of the card. The flowers on the front and my image on the back should let future clients know what I do.

```html
<!DOCTYPE html>
<html lang="en">
<head>
<meta charset="utf-8">
<title>A Quiet Wren Sang · Business Card</title>
<link rel="stylesheet" href="https://fonts.googleapis.com/css2?family=Big+Shoulders+Display:wght@300;400&family=Poiret+One&display=swap">
<style>
  :root {
    --backdrop: #b9b7b3;
    --card: #ffffff;
    --ink: #141414;
    --rule: #1a1a1a;
    --name-grey: #8d8d8d;
    --bloom-grey: #d9d6d2;
    --flower-rose: #c47a8a;
    --flower-blue: #4b4f9a;
    --flower-green: #3c5a2a;
    --flower-dark: #1e1f22;
    --jacket: #e8e2c8;
    --photo-dark: #3a2f2c;
  }
  * { margin: 0; padding: 0; box-sizing: border-box; }
  html, body { width: 1200px; height: 1001px; overflow: hidden; }
  body { background: var(--backdrop); position: relative; font-family: "Poiret One", sans-serif; color: var(--ink); }

  .card {
    position: absolute;
    background: var(--card);
    box-shadow: 6px 8px 14px rgba(0,0,0,0.35);
    overflow: hidden;
  }
  .card--front { left: 353px; top: 131px; width: 492px; height: 307px; }
  .card--back  { left: 353px; top: 472px; width: 497px; height: 305px; }

  .frame { position: absolute; inset: 0; }

  /* front */
  .floral-abstract {
    position: absolute; left: 92px; top: 107px; width: 349px; height: 139px;
    background:
      radial-gradient(circle at 30% 62%, var(--flower-rose) 0 14%, transparent 26%),
      radial-gradient(circle at 52% 62%, var(--flower-rose) 0 12%, transparent 24%),
      radial-gradient(circle at 80% 55%, var(--flower-blue) 0 16%, transparent 32%),
      radial-gradient(circle at 70% 20%, #8c8fd8 0 10%, transparent 24%),
      linear-gradient(120deg, var(--flower-green), var(--flower-dark) 55%, var(--flower-blue));
  }
  .brand-title {
    position: absolute; left: 24px; top: 54px; width: 444px;
    font-family: "Big Shoulders Display", sans-serif; font-weight: 300;
    font-size: 86px; line-height: 1; letter-spacing: -1px;
    text-align: center; white-space: nowrap;
    transform: scaleY(1.1);
  }

  /* back */
  .services-title {
    position: absolute; left: 24px; top: 20px; width: 451px;
    font-family: "Big Shoulders Display", sans-serif; font-weight: 400;
    font-size: 50px; line-height: 1; letter-spacing: 1px; white-space: nowrap;
    text-align: center;
  }
  .portrait-abstract {
    position: absolute; left: 15px; top: 95px; width: 114px; height: 177px;
    background:
      radial-gradient(ellipse at 50% 62%, var(--jacket) 0 30%, transparent 48%),
      linear-gradient(180deg, var(--photo-dark), #6b5a4a 60%, #4b4d7a);
  }
  .bloom-shape {
    position: absolute; left: 156px; top: 114px; width: 246px; height: 85px;
    border-radius: 50% 45% 50% 40%;
    background: radial-gradient(ellipse at center, var(--bloom-grey) 55%, rgba(217,214,210,0.4) 100%);
  }
  .contact {
    position: absolute; left: 336px; top: 120px;
    font-style: normal; color: var(--ink);
    font-size: 14px; line-height: 19px; letter-spacing: 2px; white-space: nowrap;
  }
  .contact .city { font-size: 10px; letter-spacing: 0.5px; }
  .website {
    position: absolute; left: 136px; top: 226px; width: 207px;
    font-size: 11px; letter-spacing: 4px; text-align: center; white-space: nowrap;
    color: var(--ink);
  }
  .owner-name {
    position: absolute; left: 86px; top: 252px; width: 266px;
    font-size: 36px; line-height: 1; letter-spacing: 8px;
    color: var(--name-grey); text-align: center; white-space: nowrap;
    background: var(--card);
  }
</style>
</head>
<body>

<section class="card card--front">
  <svg class="frame" width="492" height="307" viewBox="0 0 492 307" aria-hidden="true">
    <g stroke="var(--rule)" stroke-width="3" fill="none">
      <line x1="34" y1="27" x2="463" y2="27"/>
      <line x1="34" y1="27" x2="34" y2="48"/>
      <line x1="463" y1="27" x2="463" y2="48"/>
      <line x1="34" y1="150" x2="34" y2="277"/>
      <line x1="463" y1="150" x2="463" y2="277"/>
      <line x1="34" y1="277" x2="463" y2="277"/>
    </g>
  </svg>
  <div class="floral-abstract" role="img" aria-label="Abstract of a floral arrangement with pink roses and blue blooms"></div>
  <h1 class="brand-title">A QUIET WREN SANG</h1>
</section>

<section class="card card--back">
  <svg class="frame" width="497" height="305" viewBox="0 0 497 305" aria-hidden="true">
    <g stroke="var(--rule)" stroke-width="3" fill="none">
      <line x1="14" y1="15" x2="482" y2="15"/>
      <line x1="14" y1="15" x2="14" y2="275"/>
      <line x1="14" y1="275" x2="479" y2="275"/>
      <line x1="479" y1="76" x2="479" y2="275"/>
      <line x1="410" y1="76" x2="479" y2="76"/>
    </g>
  </svg>
  <h2 class="services-title">BESPOKE HOME SERVICES</h2>
  <div class="portrait-abstract" role="img" aria-label="Abstract portrait of the owner in a white three button butler jacket"></div>
  <div class="bloom-shape" role="img" aria-label="Soft grey flower motif"></div>
  <address class="contact">
    555 203 4417<br>
    PO BOX4082<br>
    <span class="city">BRIDLEMOOR, KT 11907</span>
  </address>
  <p class="website">FERROW TENDLE.COM</p>
  <p class="owner-name">DOV RENKO</p>
</section>

</body>
</html>
```